I need a graphic for the promotion email for our "8th Annual Brightwater Field Drills Academy" that incorporates our current logo and brand theme. I would like this graphic to funnel potentional attendees to register for a course. My perference would include a cool fire photo from our facility for the background. More information can be found on Kestrelvale.com and also our Facebook.

```html
<!DOCTYPE html>
<html lang="en">
<head>
<meta charset="utf-8">
<title>Brightwater Field Drills Academy – Email Banner</title>
<link rel="stylesheet" href="https://fonts.googleapis.com/css2?family=Orbitron:wght@700;800&family=Poppins:wght@400;700&display=swap">
<style>
  :root {
    --page-bg: #ffffff;
    --ink-white: #ffffff;
    --fire-orange: #e8541c;
    --fire-red: #e0221a;
    --ember-deep: #2a0d06;
    --night: #070504;
    --flame-hot: #f08a2a;
    --flame-glow: #ffb347;
  }
  * { box-sizing: border-box; margin: 0; padding: 0; }
  html, body {
    width: 1200px; height: 927px; overflow: hidden;
    background: var(--page-bg);
  }
  .banner {
    position: absolute; left: 90px; top: 208px;
    width: 1021px; height: 510px; overflow: hidden;
    background: var(--night);
    font-family: "Poppins", sans-serif;
    color: var(--ink-white);
  }
  .banner__photo {
    position: absolute; inset: 0;
    background:
      radial-gradient(ellipse 40% 55% at 82% 40%, var(--flame-glow) 0%, var(--flame-hot) 25%, rgba(200,60,10,0.6) 55%, rgba(0,0,0,0) 80%),
      radial-gradient(ellipse 60% 30% at 60% 100%, rgba(240,120,30,0.85) 0%, rgba(160,40,10,0.5) 50%, rgba(0,0,0,0) 85%),
      linear-gradient(90deg, var(--night) 0%, var(--ember-deep) 30%, #6a1f08 60%, #b2380e 100%);
  }
  .brand {
    position: absolute; left: 51px; top: 55px;
    display: flex; align-items: center; gap: 28px;
  }
  .brand__mark {
    width: 84px; height: 84px; border-radius: 50%;
    border: 3px solid var(--fire-orange);
  }
  .brand__name {
    font-family: "Orbitron", sans-serif; font-weight: 700;
    font-size: 22px; letter-spacing: 6px; color: var(--ink-white);
  }
  .kicker {
    position: absolute; left: 51px; top: 154px;
    font-size: 17px; letter-spacing: 0.3px;
  }
  .headline {
    position: absolute; left: 51px; top: 190px;
    font-family: "Orbitron", sans-serif; font-weight: 800;
    font-size: 34px; line-height: 39px; text-transform: uppercase;
    letter-spacing: 1px;
  }
  .divider {
    position: absolute; left: 48px; top: 331px;
    width: 380px; height: 3px;
    background: linear-gradient(90deg, rgba(224,34,26,0.2), var(--fire-red) 35%, var(--fire-red) 65%, rgba(224,34,26,0));
    box-shadow: 0 0 8px var(--fire-red);
  }
  .tagline {
    position: absolute; left: 55px; top: 341px;
    font-size: 15.5px; letter-spacing: 0.2px;
  }
  .cta {
    position: absolute; left: 75px; top: 390px;
    width: 222px; height: 36px; border-radius: 18px;
    background: var(--fire-orange);
    border: 1.5px solid #ffd2b8;
    box-shadow: 0 0 14px rgba(232,84,28,0.8);
    display: flex; align-items: center; justify-content: center; gap: 14px;
    font-weight: 700; font-size: 17px; color: var(--ink-white);
    text-decoration: none;
  }
</style>
</head>
<body>
  <section class="banner">
    <div class="banner__photo" role="img" aria-label="Firefighters in breathing gear advancing toward a burning multi-storey training tower at the facility"></div>

    <div class="brand">
      <div class="brand__mark"></div>
      <span class="brand__name">KESTRELVALE RESCUE</span>
    </div>

    <p class="kicker">NOW OPEN FOR REGISTRATION</p>

    <h1 class="headline">8th Annual<br>Brightwater Field<br>Drills Academy</h1>

    <div class="divider"></div>

    <p class="tagline">HANDS-ON INDUSTRIAL FIRE &amp; RESCUE TRAINING</p>

    <a class="cta" href="#">REGISTER NOW
      <svg width="36" height="18" viewBox="0 0 36 18" aria-hidden="true">
        <path d="M1 9 H33 M25 2 L33 9 L25 16" fill="none" stroke="#ffffff" stroke-width="2.5" stroke-linecap="round" stroke-linejoin="round"/>
      </svg>
    </a>
  </section>
</body>
</html>
```